Beauty Salon Industry - Web Design Project

zTrellis is a well-funded start up developing an Online Marketing Platform for small businesses in Europe.
We require a large number of high quality business web designs for our business website builder. Our business websites are seamlessly integrated into our Online Marketing systems and therefore it is important for designers to comply with our Design Guidelines.
This is our second contest and it will focus on the beauty salon industry. We will be running contents every 2-3 weeks for a new industry. Last month, we ran a contest for Builder website designs with 3 top prizes (plus £10 per variation) and we also paid out £25 per design for 20+ entries from designers who did not win the top prizes. So we encourage all entries!
We have included a wire frame this time to encourage you to be as creative as possible with your designs and layout while respecting the following guidelines:
1) You CAN change the layout as much as you like. If you think a vertical menu would look better, then use it. If you think the design would benefit from moving an element to a different location, then you can do that too.
2) You must include ALL the elements in the wire frame in your design.(e.g. latest 2 news entries, a testimonial, 1 gallery image, carousel etc...). Please make sure you have looked through the wire frame and know what is required. Entries that do not include all the elements will not qualify to win.
3) So remember, you CAN change the layout as much as you like but DO NOT remove any elements nor move them to a different page.
4) You may change the size and style of the carousel image. We would like to see as many variations of this as possible.
We are rewarding 3 prizes, and would like the winning designer to design the internal pages to the new design.
As always, if we think your designs could be incorporated into our system, but you do not win the competition, we will reward £25. Therefore, we encourage designers to submit as many designs as possible as we may award up to 25 designs.
Judging criteria : -
1) Visual Design
2) Layout must adhere to best practices and wireframe. If you decide to move elements around significantly please provide reason
3) Functional, informative and drives calls to action
Updates
As usual:
1st place = £350
2nd place = £250
3rd place = £150
Good luck!
Very happy with all the designs submitted so far, and will provide feedback ASAP.
We would like to see you try arranging the elements differently. So please try different navigation types and layouts.
Thanks
Morris
Prize funds for 1st place has been slightly increased.
Thanks
Morris
We have already had some amazing designs submitted. Thanks.
Remember to play with the layout of the elements and try designs with a carousel/slider that is in portrait not just in landscape.
Thanks everyone!
Morris
Hi everyone, we are really enjoying looking through the designs.
We have one NEW requirement. If you have used an image from http://www.quarnex-demo.net/ in your design, could you please replace it with another.
We are not associated with them.
Thank you.
I have just sent a poll around the office to vote on all the designs and hope to have the results soon.
Good luck and I hope to see all your great designs for our next project in a couple of weeks.
Morris
Hi everyone, we hope you have had a good holiday season. We will be rewarding the prizes very soon, hopefully today or tomorrow.
Thanks
Morris
We are currently going through all the designs that did not win our competition and will be contacting the designers of the designs we would like to use in our system, so please keep an eye on your inbox over the next few days.
Thank you
Morris
Target Market(s)
Beauty Salon Industry
Industry/Entity Type
Beauty Salon
Look and feel
Each slider illustrates characteristics of the customer's brand and the style your logo design should communicate.

```html
<!DOCTYPE html>
<html lang="en">
<head>
<meta charset="utf-8">
<title>Velvet Tress – Hair and Urban Spa</title>
<link rel="stylesheet" href="https://fonts.googleapis.com/css2?family=Ubuntu:wght@400;500&family=Ubuntu+Condensed&family=Noto+Serif:ital,wght@0,400;1,400&family=Graduate&display=swap">
<style>
:root{
  --purple:#8a66b0;
  --purple-dark:#6b4c8f;
  --purple-deep:#5a3f7a;
  --sage:#6f9c85;
  --sage-light:#bcc5a7;
  --gold:#c7a64f;
  --tan:#d8bf8a;
  --tan-dark:#8a6f3d;
  --teal:#1fb5a8;
  --mauve:#a88686;
  --ink:#333;
  --muted:#5b4452;
  --page:#f1f1f1;
}
*{box-sizing:border-box;margin:0;padding:0}
html,body{width:1045px;height:1200px;overflow:hidden;background:var(--page)}
.page{position:absolute;left:0;top:0;width:1000px;height:1141px;transform:scale(1.045,1.0517);transform-origin:0 0;
  font-family:"Ubuntu",sans-serif;color:var(--ink);
  background:radial-gradient(ellipse at 70% 20%,#fbfbfb 0%,#e9e9e9 60%,#f4f4f4 100%)}
.abs{position:absolute}
.brand{left:60px;top:28px;display:flex;align-items:center;gap:12px}
.brand-dot{width:40px;height:40px;border-radius:50%;background:var(--purple)}
.brand-name{font-family:"Ubuntu",sans-serif;font-size:30px;color:var(--purple);line-height:1.05;white-space:nowrap}
.brand-name small{display:block;font-size:17px}
.phone{left:780px;top:14px;width:165px;text-align:center;font-family:"Noto Serif",serif;font-size:21px;color:#3a2a30;white-space:nowrap}
.book-now{left:783px;top:43px;width:157px;height:47px;border-radius:6px;background:var(--teal);border:3px solid #8fe0d6;
  color:#fff;font-family:"Ubuntu Condensed",sans-serif;font-size:25px;letter-spacing:-0.5px;white-space:nowrap;overflow:hidden;
  text-align:center;line-height:41px;box-shadow:0 2px 3px rgba(0,0,0,.25)}
.rule{left:60px;top:104px;width:882px;height:3px;border-top:1px dashed #cfcfcf;border-bottom:1px dashed #cfcfcf}
.rule-star{left:487px;top:92px}
.nav{left:60px;top:135px;width:202px;height:215px;background:var(--purple);border:3px solid #b79fd1;border-radius:10px 4px 10px 4px;padding:14px 14px 0 20px}
.nav a{display:block;color:#fff;text-decoration:none;font-size:15px;height:27px;line-height:26px;border-bottom:1px dashed rgba(255,255,255,.45)}
.nav a:last-child{border:none}
.intro{left:60px;top:360px;width:202px;height:340px;background:var(--sage);border-radius:12px;padding:40px 12px 0 12px;color:#fff}
.intro-pin{left:91px;top:12px;width:20px;height:20px;border-radius:50%;background:#222;border:3px solid #999}
.intro h2{font-weight:400;font-size:17px;line-height:18px;margin-bottom:10px}
.intro p{font-size:11px;line-height:18px;margin-bottom:12px}
.tag{display:inline-block;flex:none;white-space:nowrap;font-family:"Noto Serif",serif;font-size:11px;line-height:14px;color:#fff;padding:3px 8px;border:1px solid rgba(255,255,255,.6);box-shadow:2px 2px 0 rgba(0,0,0,.15)}
.tag-line{display:flex;align-items:center;gap:6px;justify-content:center}
.tag-line::before,.tag-line::after{content:"";flex:0 1 55px;min-width:8px;border-top:3px double currentColor;opacity:.5}
.intro .tag-line{position:absolute;left:0;right:0;bottom:12px}
.intro .tag{background:#5b8670}
.gallery{left:60px;top:710px;width:202px;height:257px;background:var(--gold);text-align:center;color:#fff}
.gallery h3{font-weight:400;font-size:19px;margin-top:8px}
.gallery-photo{left:5px;top:35px;width:190px;height:180px;border:2px solid #eee;background:linear-gradient(160deg,#8c8686 0%,#3a2a24 55%,#c9c3bf 100%)}
.gallery .tag-line{position:absolute;left:0;right:0;bottom:12px;color:#7a5f25}
.gallery .tag{background:#8f7a3e;color:#fff}
.slider{left:272px;top:135px;width:478px;height:381px;background:linear-gradient(120deg,#6e4a22 0%,#b8865a 40%,#e2b99a 55%,#a8743e 75%,#5a3818 100%)}
.thumbs{left:278px;top:140px;width:77px;height:370px;background:#2b1e17;border-radius:4px}
.thumb{position:absolute;left:5px;width:67px;height:80px;border:1px solid #bbb}
.arrow{position:absolute;left:30px;width:0;height:0;border-left:8px solid transparent;border-right:8px solid transparent}
.promo{left:760px;top:135px;width:181px;height:265px;background:var(--purple)}
.promo-photo{left:5px;top:5px;width:172px;height:100px;background:linear-gradient(180deg,#f2f4f8,#9fb0d3 60%,#e7ebf3)}
.price{left:40px;top:116px;width:100px;height:32px;background:#e6dcef;border:2px solid #fff;border-radius:6px;text-align:center;
  font-family:"Noto Serif",serif;font-size:24px;color:var(--purple-deep);line-height:28px}
.promo p{position:absolute;left:9px;top:160px;width:166px;font-size:11.5px;color:#fff;line-height:14px}
.appointment{left:5px;top:193px;width:172px;height:67px;background:var(--purple-deep);font-family:"Graduate",serif;color:#fff;font-size:19px;line-height:19px;padding:8px 8px 0 10px;white-space:nowrap}
.appointment span{display:block;text-align:right}
.address{left:760px;top:400px;width:181px;height:116px;background:var(--tan);padding:12px 14px;color:#fff}
.address h4{font-family:"Noto Serif",serif;font-weight:400;color:#222;font-size:16px;margin-bottom:6px;white-space:nowrap}
.address p{font-size:11px;line-height:16px}
.address .tag-line{margin-top:6px;color:#8a6f3d}
.address .tag{background:#a88a4e}
.hours{left:760px;top:530px;width:181px;height:163px;background:var(--sage-light);padding:8px 5px 0 5px}
.hours h4{font-family:"Noto Serif",serif;font-weight:400;font-size:16px;color:#3e4a35;margin-left:5px;margin-bottom:5px;white-space:nowrap}
.hours table{width:171px;border-collapse:collapse;background:#dfe4cf;font-size:11px;color:#222}
.hours td{height:20.7px;padding:0 8px;border-bottom:1px dashed #fff;white-space:nowrap}
.hours td:last-child{text-align:right}
.quote{left:272px;top:530px;width:478px;height:130px}
.qmark{position:absolute;font-family:"Noto Serif",serif;font-size:96px;color:var(--mauve);line-height:1}
.quote blockquote{position:absolute;left:56px;top:30px;width:372px;font-family:"Noto Serif",serif;font-style:italic;font-size:14px;line-height:20px;color:var(--muted)}
.quote cite{display:block;text-align:right}
.quote .tag-line{position:absolute;left:0;right:0;top:104px;color:#999}
.quote .tag,.more-news .tag{background:var(--mauve)}
.news-head{left:272px;top:686px;width:478px;display:flex;align-items:center;gap:8px;color:var(--purple-dark);font-family:"Noto Serif",serif;font-size:16px;font-weight:400;white-space:nowrap}
.news-head::before,.news-head::after{content:"";flex:1;border-top:3px double #b9a4cb}
.news{top:722px;width:235px;height:90px}
.news h5{font-weight:400;font-size:15px;color:#111;margin-bottom:8px;white-space:nowrap}
.news-date{position:absolute;left:0;top:30px;width:56px;height:56px;border-radius:50%;background:var(--purple-dark);color:#fff;text-align:center;font-size:11px;line-height:13px;padding-top:8px}
.news-date b{display:block;font-size:14px;font-weight:500}
.news p{position:absolute;left:65px;top:27px;width:165px;font-size:10px;line-height:14.5px;color:#222}
.news-divider{left:501px;top:716px;height:92px;border-left:1px dotted #888}
.more-news{left:272px;top:823px;width:478px;color:#999}
.partners{left:60px;top:977px;width:881px;height:136px;background:var(--tan);padding:6px}
.partners-inner{width:100%;height:100%;border:1px solid #f1e3c3;display:flex;align-items:center;justify-content:space-around;
  font-family:"Ubuntu",sans-serif;font-size:34px;color:#6d5e49;white-space:nowrap}
.footer{left:788px;top:1124px;font-size:10px;color:#333;white-space:nowrap}
.footer span{margin-left:14px}
</style>
</head>
<body>
<div class="page">
  <header>
    <div class="abs brand"><span class="brand-dot"></span><div class="brand-name">Velvet Tress<small>Hair and Urban Spa</small></div></div>
    <div class="abs phone">020 7946 0182</div>
    <div class="abs book-now">BOOK NOW</div>
    <div class="abs rule"></div>
    <svg class="abs rule-star" width="26" height="26" viewBox="0 0 24 24"><polygon points="12,1 15,9 23,9 16.5,14 19,22 12,17 5,22 7.5,14 1,9 9,9" fill="#b7bd9d"/></svg>
  </header>

  <nav class="abs nav">
    <a href="#">Home</a><a href="#">Services</a><a href="#">Gallery</a><a href="#">Testimonials</a><a href="#">News</a><a href="#">About Us</a><a href="#">Contact Us</a>
  </nav>

  <section class="abs intro">
    <span class="abs intro-pin"></span>
    <h2>LET OUR HAIR AND BEAUTY SKILLS BLOW YOU AWAY</h2>
    <p>Velvet Tress is a passionate creative team, dedicated to delivering a second to none, personal salon experience that will 'blow' your mind.</p>
    <p>Where ultimate hairdressing comes hand-in-hand with style. glamour, fashion, innovation and skill to create an exquisite salon experience in the heart od London.</p>
    <div class="tag-line"><span class="tag">MORE</span></div>
  </section>

  <section class="abs gallery">
    <h3>OUR GALLERY</h3>
    <div class="abs gallery-photo" role="img" aria-label="Gallery photo of a model with long dark curly hair"></div>
    <div class="tag-line"><span class="tag">VIEW GALLERY</span></div>
  </section>

  <section class="abs slider" role="img" aria-label="Carousel photo of a model with long golden wavy hair"></section>
  <div class="abs thumbs">
    <span class="arrow" style="top:6px;border-bottom:8px solid #fff"></span>
    <span class="thumb" role="img" aria-label="Thumbnail of blonde hairstyle" style="top:20px;background:linear-gradient(#c08a4e,#6d4524)"></span>
    <span class="thumb" role="img" aria-label="Thumbnail of auburn hairstyle" style="top:104px;background:linear-gradient(#d9b7a8,#8b4a36)"></span>
    <span class="thumb" role="img" aria-label="Thumbnail of brunette hairstyle" style="top:188px;background:linear-gradient(#7a5a4a,#2e1d17)"></span>
    <span class="thumb" role="img" aria-label="Thumbnail of red-brown hairstyle" style="top:272px;background:linear-gradient(#a87a78,#5a2a2c)"></span>
    <span class="arrow" style="top:356px;border-top:8px solid #fff"></span>
  </div>

  <aside class="abs promo">
    <div class="abs promo-photo" role="img" aria-label="Photo of wrapped gift boxes with blue ribbons"></div>
    <div class="abs price">£25</div>
    <p>Complimentary gift for first-time clients!</p>
    <div class="abs appointment">BOOK<br>APPOINTMENT<span>NOW</span></div>
  </aside>

  <aside class="abs address">
    <h4>VELVET ADDRESS:</h4>
    <p>12 Larkmoor Lane<br>London<br>W1X 9QT</p>
    <div class="tag-line"><span class="tag">VIEW MAP</span></div>
  </aside>

  <aside class="abs hours">
    <h4>BUSINESS HOURS</h4>
    <table>
      <tr><td>MON</td><td>9 AM - 5 PM</td></tr>
      <tr><td>TUE</td><td>9 AM - 5 PM</td></tr>
      <tr><td>WED</td><td>9 AM - 5 PM</td></tr>
      <tr><td>THU</td><td>9 AM - 5 PM</td></tr>
      <tr><td>FRI</td><td>9 AM - 5 PM</td></tr>
      <tr><td>SAT</td><td>9 AM - 5 PM</td></tr>
    </table>
  </aside>

  <section class="abs quote">
    <span class="qmark" style="left:0;top:-4px">&ldquo;</span>
    <blockquote>My hairstylist, Maribel, was truly amazing. She listened to exactly what I wanted, but also told me exactly what...<cite>-Ineza Halvorsen</cite></blockquote>
    <span class="qmark" style="left:434px;top:50px">&rdquo;</span>
    <div class="tag-line"><span class="tag">MORE</span></div>
  </section>

  <h3 class="abs news-head">★ LATEST NEWS ★</h3>
  <article class="abs news" style="left:272px">
    <h5>Book Now for Christmas</h5>
    <div class="news-date">DEC<b>01</b>2011</div>
    <p>Our salon is usually very busy for the two weeks before Christmas, so please book early: call 020 7946 0182. or contact us.</p>
  </article>
  <div class="abs news-divider"></div>
  <article class="abs news" style="left:511px">
    <h5>Want to be a hair model?</h5>
    <div class="news-date">DEC<b>09</b>2011</div>
    <p>We always need models for our portfolio. If you want to become one please contact us.</p>
  </article>
  <div class="abs more-news tag-line"><span class="tag">MORE NEWS</span></div>

  <section class="abs partners">
    <div class="partners-inner"><span>Lumivelle</span><span>Corvane</span><span>Pell &amp; Pell</span><span>Ostermark</span></div>
  </section>

  <footer class="abs footer">Managed by zTrellis.com<span>Admin</span></footer>
</div>
</body>
</html>
```